Poster/Signage - Awards/Honour Board

We are a professional organisation delivering general practice education and training in Australia.

We need to update our awards honour board.

It consists of two panels, which are encased in clear acrylic on a wall.

The design needs to incorporate both panels.

Attached is an example of a layout and the required content. It is just an example and doesn’t have to be laid out this way. It does however need to incorporate all content copy and elements provided in this example and be legible to read from at least 90cms distance.

Our corporate colours need to be used in the design and we would like to have some kind of background graphic that stretches across the two panels (and allows for the gap in between). Use of the dots in our logo is one possible option.

The design must be fresh, contemporary, clean, uncluttered and sophisticated.

PLEASE NOTE: The attached example is an example only, both in terms of design and layout. No design skills of any kind have been applied in this example! So go ahead and be creative!

Colours:
Green 1: R:0, G: 144, B: 68
Green 2: R:240, G: 160, B: 671

Size: (also see diagram attached)
Left panel: 800mm high x 210mm wide
Right panel: 800mm high x 450mm wide
Gap between panels: 800mm high x 73mm wide

Attached:
• Example layout with content (PDF & Word)
• Panel sizes diagram (PDF)
• GP Meridale logo
• Government logo (sub-logo)
• Images

Thanks and good luck!

Project Deadline Extended
Reason: Hi Thanks to all designers who have made submissions within the requested deadline. We have decided to extend the deadline by 5 days as in reflection closing on the weekend wasn't ideal in terms of being able to review designs and provide feedback. Regarding designs so far, we are hoping for a contemporary, fresh, clean look that maximises 'white space'. We realise there is a lot of information to be included in a small space, and at the same time achieve readability, so getting a lot of 'white space' may be difficult. Basically we are hoping the design will look very clean and uncluttered, but sophisticated. In terms of colour palette, please use the logos colours where you can, but feel free to incorporate lots of whites, greys or other neutrals. Using dots from the logo in some form would also be good. Thank you again, and I will be in touch next week with further feedback once I confer with my colleagues. Joan

```html
<!DOCTYPE html>
<html lang="en">
<head>
<meta charset="utf-8">
<title>GP Meridale Awards Honour Board</title>
<link href="https://fonts.googleapis.com/css2?family=Open+Sans:wght@400&family=PT+Sans:ital,wght@0,400;0,700;1,400;1,700&display=swap" rel="stylesheet">
<style>
:root{
  --backdrop:#2a2a2a;
  --board:#ffffff;
  --corner:#26373b;
  --teal:#2a9d80;
  --ink:#1f2d35;
  --text:#2b2b2b;
  --rule:#c9cdcf;
  --band:#e4e6e7;
  --frame:#4a5558;
}
*{box-sizing:border-box;margin:0;padding:0}
html,body{width:1200px;height:1000px;overflow:hidden;background:var(--backdrop);font-family:"PT Sans",sans-serif}
.board{position:absolute;left:195px;top:12px;width:892px;height:965px;background:var(--board);border:2px solid var(--frame);overflow:hidden}
.board__band{position:absolute;left:0;top:110px;width:100%;height:770px;background:linear-gradient(90deg,#fff 0,#fff 25%,var(--band) 36%,#f4f5f5 48%,#fff 60%)}
.corner{position:absolute;width:56px;height:56px;background:var(--corner)}
.corner--tl{left:0;top:0;border-bottom-right-radius:56px}
.corner--tr{right:0;top:0;border-bottom-left-radius:56px}
.corner--bl{left:0;bottom:0;border-top-right-radius:56px}
.corner--br{right:0;bottom:0;border-top-left-radius:56px}
.title{position:absolute;left:0;top:14px;width:100%;text-align:center;font-family:"Open Sans",sans-serif;font-weight:400;font-size:46px;letter-spacing:1px;color:var(--teal)}
.title-rule{position:absolute;top:76px;height:2px;background:var(--ink)}
.title-rule--l{left:176px;width:230px}
.title-rule--r{left:506px;width:230px}
.title-flourish{position:absolute;left:418px;top:70px;width:76px;height:16px;background:linear-gradient(90deg,transparent,#cfd3d4,transparent);border-radius:8px}
.label{position:absolute;left:2px;width:212px;background:#fff;box-shadow:0 4px 5px -2px rgba(0,0,0,.35);display:flex;align-items:center}
.label__name{width:108px;text-align:center;font-style:italic;font-weight:700;font-size:13px;line-height:16px;color:var(--ink)}
.photo{position:absolute;left:110px;width:98px;height:98px;border:3px solid #fff;box-shadow:0 1px 4px rgba(0,0,0,.55)}
.entry{position:absolute;left:310px;width:576px;background:#fff;padding:0 6px 6px}
.entry__lead{font-weight:700;font-size:13px;line-height:17px;color:var(--ink);text-align:justify;padding:4px 0 5px;border-bottom:2px solid var(--rule);box-shadow:0 3px 3px -2px rgba(0,0,0,.25)}
.entry__year{margin-top:10px;font-style:italic;font-weight:700;font-size:13px;color:var(--teal);line-height:15px}
.entry__year--tight{margin-top:4px}
.entry__text{font-size:11px;line-height:13px;color:var(--text)}
.footer-mark{position:absolute;left:320px;top:880px;width:86px;height:78px;background:#2d3b3e;display:flex;align-items:flex-end;justify-content:center;padding-bottom:6px}
.footer-mark__name{font-size:9px;letter-spacing:1.5px;color:#fff;font-weight:400;white-space:nowrap}
.footer-sub{position:absolute;left:430px;top:914px;width:170px;text-align:center;color:var(--ink);white-space:nowrap}
.footer-sub__top{font-size:10.5px;font-weight:700;line-height:13px;border-bottom:1px solid var(--ink);padding-bottom:2px}
.footer-sub__bottom{font-size:10px;font-weight:700;line-height:12px;padding-top:2px}
</style>
</head>
<body>
<main class="board">
  <div class="board__band"></div>
  <div class="corner corner--tl"></div><div class="corner corner--tr"></div>
  <div class="corner corner--bl"></div><div class="corner corner--br"></div>

  <h1 class="title">GP MERIDALE AWARDS</h1>
  <div class="title-rule title-rule--l"></div>
  <div class="title-flourish"></div>
  <div class="title-rule title-rule--r"></div>

  <div class="label" style="top:114px;height:102px"><p class="label__name">Dr Martin Hale Outstanding Achievement Award</p></div>
  <div class="photo" role="img" aria-label="Portrait photo of Dr Laura Bennet" style="top:114px;background:linear-gradient(160deg,#3a2e2a,#8a6e60 55%,#2a2422)"></div>
  <section class="entry" style="top:110px">
    <p class="entry__lead">In honour of GP Meridale’s late Director of Training, Dr Martin Hale, this is GP Meridale’s peak award, recognising outstanding achievement by a GP Meridale staff member, supervisor or current/recently completed registrar.</p>
    <p class="entry__year">2013 Dr Laura Bennet</p>
    <p class="entry__text">In 2013, Dr Laura Bennet, was awarded the Dr Martin Hale Outstanding Achievement Award for her commitment to general practice education. In her role as a GP Meridale medical educator Laura has embraced new technologies to create innovative modes of education delivery. She is an inspiring ambassador of the general practice profession and a dedicated educator.</p>
    <p class="entry__year">2012 Dr Peter Andros</p>
    <p class="entry__text">For his commitment to enhancing the GP training for National Defence Force registrars and promotion of the general practice profession.</p>
    <p class="entry__year entry__year--tight" style="margin-top:6px">2011 Dr Claire Whitby</p>
    <p class="entry__text">For her involvement in the development of an Indigenous health clinic in Kelsford.</p>
  </section>

  <div class="label" style="top:339px;height:106px"><p class="label__name">The Outstand-ing Academic Achievement by a Registrar Award</p></div>
  <div class="photo" role="img" aria-label="Portrait photo of Dr Daniel Corrie" style="top:342px;background:linear-gradient(160deg,#c9d3d6,#b98f78 50%,#6b5a52)"></div>
  <section class="entry" style="top:338px">
    <p class="entry__lead">This award recognises the achievements of the GP Meridale registrar who completed the Royal College of Family Practice (RCFP) fellowship exam with the highest overall score in a given year.</p>
    <p class="entry__year">2013 Dr Daniel Corrie</p>
    <p class="entry__text">The 2013 recipient of the Outstanding Academic Achievement by a Registrar Award was completed general pathway registrar, Dr Daniel Corrie. Daniel is now a fellowed GP, practising in one of his former training practices in southern Harbourton.</p>
    <p class="entry__year entry__year--tight">2012 Dr Grace Tanaka</p>
    <p class="entry__year entry__year--tight">2011 Dr Emma Pryce</p>
  </section>

  <div class="label" style="top:504px;height:104px"><p class="label__name">GP Meridale Supervisor of the Year Award</p></div>
  <div class="photo" role="img" aria-label="Portrait photo of Dr Ruth Alder" style="top:507px;background:linear-gradient(160deg,#d8b060,#c99a70 50%,#7a5a3a)"></div>
  <section class="entry" style="top:505px">
    <p class="entry__lead">This award recognises the dedication and on- going commitment to the provision of quality general practice education and training by a GP Meridale supervisor.</p>
    <p class="entry__year" style="margin-top:8px">2013 Dr Ruth Alder</p>
    <p class="entry__text">The inaugural GP Meridale Supervisor of the Year Award was presented to Dr Ruth Alder – a GP supervisor with over 25 years teaching experience. A practising GP at the Eastvale Aboriginal Medical Service, this award recognises her ongoing commitment to general practice education and teaching approach.</p>
  </section>

  <div class="label" style="top:626px;height:107px"><p class="label__name">GP Meridale Practice Manager of the Year Award</p></div>
  <div class="photo" role="img" aria-label="Portrait photo of Nadia Fenwick" style="top:629px;background:linear-gradient(160deg,#d9c48a,#c8a886 50%,#5a4a3a)"></div>
  <section class="entry" style="top:626px">
    <p class="entry__lead">Awarded to a GP Meridale Practice Manager in recognition of their dedication and on - going commitment to the provision of quality general practice education and training.</p>
    <p class="entry__year" style="margin-top:8px">2013: Nadia Fenwick</p>
    <p class="entry__text">In 2013, the inaugural GP Meridale Practice Manager of the Year Award was presented to Nadia Fenwick, practice manager at Ashgrove Family Medical Practice in recognition of her instrumental role in fostering a learning culture within the practice.</p>
  </section>

  <div class="label" style="top:758px;height:105px"><p class="label__name">GP Meridale Staff Member of the Year Award</p></div>
  <div class="photo" role="img" aria-label="Portrait photo of Dr Helen Marsh" style="top:762px;background:linear-gradient(160deg,#4a3a34,#b08878 50%,#3a2a2a)"></div>
  <section class="entry" style="top:756px">
    <p class="entry__lead">This award recognises the dedication and on - going commitment to the provision of quality - general practice education and training by a GP Meridale staff member.</p>
    <p class="entry__year" style="margin-top:8px">2013: Dr Helen Marsh (PhD)</p>
    <p class="entry__text">The recipient of the inaugural GP Meridale Staff Member of the Year Award was Dr Helen Marsh (PhD). This award recognises Helen’s role in managing the administration of over 380 GP registrars, and the critical role she plays in their successful completion of the GP training program.</p>
  </section>

  <div class="footer-mark"><span class="footer-mark__name">GP MERIDALE</span></div>
  <div class="footer-sub">
    <p class="footer-sub__top">Commonwealth Health Office</p>
    <p class="footer-sub__bottom">Practice Training Agency Limited</p>
  </div>
</main>
</body>
</html>
```